Batch #27 - MEN'S NATURAL THERAPEUTIC INTIMATE WASH

Men's Natural Therapeutic INTIMATE Wash
BATCH #27

Design a 4 oz. stand up tube with flip top cap...
To be packaged in a carton/box

Formula contains Tea Tree OIL
Aloe Vera Gel
Coconut Oil

PRODUCT IS A WASH/SOAP

Helps with
- Jock Itch (tinea cruris)
- Skin Rashes
- Candida
- Itchy Skin

COLORS ON TUBE: Gray, Black, Lime Electric Green and Blue

PRODUCT FOR MEN!

Target Market(s)

MEN

Industry/Entity Type

Retail

Font styles to use
Sans Serif

Colors
9bcb3b
abd036
33a6d7
000000
c9c9c9

Requirements
Must have
• Colors... black, gray, electric green and blue
Nice to have
• Needs to look masculine appeal to the male consumer

```html
<!DOCTYPE html>
<html lang="en">
<head>
<meta charset="utf-8">
<title>Men's Natural Therapeutic Intimate Wash – Tube Range</title>
<link rel="stylesheet" href="https://fonts.googleapis.com/css2?family=Marcellus&family=Roboto+Condensed:wght@500;700&family=Playfair+Display:wght@400&display=swap">
<style>
  :root {
    --canvas: #ffffff;
    --tube-gray-light: #d6d6d6;
    --tube-gray: #c6c6c6;
    --tube-gray-dark: #b3b3b3;
    --crimp: #ececec;
    --band-black: #161616;
    --divider-line: #e4e4e4;
    --ink: #161616;
    --brand-ink: #ffffff;
    --cap: #f1f1f1;
    --cap-edge: #dcdcdc;
    --lime: #b2d627;
    --green: #2bd67b;
    --cyan: #27d3d3;
    --amber: #d8a22a;
  }
  * { box-sizing: border-box; margin: 0; padding: 0; }
  html, body { width: 1200px; height: 687px; overflow: hidden; background: var(--canvas); }
  .range { position: relative; width: 1200px; height: 687px; }

  .tube { position: absolute; top: 42px; width: 256px; height: 456px; }
  .tube--lime  { left: 55px;  --accent: var(--lime); }
  .tube--green { left: 333px; --accent: var(--green); }
  .tube--cyan  { left: 612px; --accent: var(--cyan); }
  .tube--amber { left: 888px; --accent: var(--amber); }

  .tube-body {
    position: absolute; left: 0; top: 0; width: 256px; height: 346px;
    clip-path: polygon(0 0, 100% 0, 91% 100%, 9% 100%);
    overflow: hidden;
  }
  .tube-pattern {
    position: absolute; inset: 0;
    background: linear-gradient(160deg, var(--tube-gray-light) 0%, var(--tube-gray) 45%, var(--tube-gray-dark) 75%, var(--tube-gray) 100%);
  }
  .tube-crimp { position: absolute; left: 0; top: 0; width: 100%; height: 10px; background: var(--crimp); }

  .brand-band {
    position: absolute; left: 0; top: 108px; width: 100%; height: 137px;
    background: var(--band-black);
    display: flex; align-items: center; justify-content: center;
  }
  .brand-name {
    font-family: "Marcellus", serif;
    color: var(--brand-ink);
    font-size: 27px; letter-spacing: 0.5px;
    margin-top: 4px;
  }
  .band-rule { position: absolute; left: 0; top: 245px; width: 100%; height: 10px; background: var(--divider-line); }

  .variant-band {
    position: absolute; left: 33px; top: 255px; width: 189px; height: 55px;
    background: var(--accent);
    display: flex; align-items: center;
  }
  .variant-number {
    width: 46px; text-align: center; color: var(--ink);
    display: flex; flex-direction: column; align-items: center;
  }
  .variant-number .no {
    font-family: "Playfair Display", serif; font-size: 10px;
    border-bottom: 1px solid var(--ink); padding: 0 2px 1px; line-height: 11px;
  }
  .variant-number .num {
    font-family: "Roboto Condensed", sans-serif; font-weight: 700; font-size: 15px; line-height: 18px;
  }
  .variant-divider { width: 1px; height: 40px; background: var(--ink); }
  .product-name {
    padding-left: 10px;
    font-family: "Roboto Condensed", sans-serif; font-weight: 700;
    font-size: 11.5px; line-height: 13.5px; color: var(--ink);
  }

  .tube-cap {
    position: absolute; left: 53px; top: 344px; width: 167px; height: 111px;
    background: var(--cap);
    border: 1px solid var(--cap-edge);
    border-radius: 2px 2px 8px 8px;
  }
  .cap-lid {
    position: absolute; left: 42px; top: 26px; width: 82px; height: 34px;
    border: 1px solid var(--cap-edge); border-top: none; border-radius: 0 0 6px 6px;
  }
</style>
</head>
<body>
<main class="range">

  <article class="tube tube--lime">
    <div class="tube-body">
      <div class="tube-pattern" role="img" aria-label="Faceted gray polygon pattern"></div>
      <div class="tube-crimp"></div>
      <div class="brand-band"><span class="brand-name">BRAND NAME</span></div>
      <div class="band-rule"></div>
      <div class="variant-band">
        <div class="variant-number"><span class="no">NO.</span><span class="num">27</span></div>
        <div class="variant-divider"></div>
        <p class="product-name">Men's<br>Natural Therapeutic<br>INTIMATE Wash</p>
      </div>
    </div>
    <div class="tube-cap"><div class="cap-lid"></div></div>
  </article>

  <article class="tube tube--green">
    <div class="tube-body">
      <div class="tube-pattern" role="img" aria-label="Faceted gray polygon pattern"></div>
      <div class="tube-crimp"></div>
      <div class="brand-band"><span class="brand-name">BRAND NAME</span></div>
      <div class="band-rule"></div>
      <div class="variant-band">
        <div class="variant-number"><span class="no">NO.</span><span class="num">27</span></div>
        <div class="variant-divider"></div>
        <p class="product-name">Men's<br>Natural Therapeutic<br>INTIMATE Wash</p>
      </div>
    </div>
    <div class="tube-cap"><div class="cap-lid"></div></div>
  </article>

  <article class="tube tube--cyan">
    <div class="tube-body">
      <div class="tube-pattern" role="img" aria-label="Faceted gray polygon pattern"></div>
      <div class="tube-crimp"></div>
      <div class="brand-band"><span class="brand-name">BRAND NAME</span></div>
      <div class="band-rule"></div>
      <div class="variant-band">
        <div class="variant-number"><span class="no">NO.</span><span class="num">27</span></div>
        <div class="variant-divider"></div>
        <p class="product-name">Men's<br>Natural Therapeutic<br>INTIMATE Wash</p>
      </div>
    </div>
    <div class="tube-cap"><div class="cap-lid"></div></div>
  </article>

  <article class="tube tube--amber">
    <div class="tube-body">
      <div class="tube-pattern" role="img" aria-label="Faceted gray polygon pattern"></div>
      <div class="tube-crimp"></div>
      <div class="brand-band"><span class="brand-name">BRAND NAME</span></div>
      <div class="band-rule"></div>
      <div class="variant-band">
        <div class="variant-number"><span class="no">NO.</span><span class="num">27</span></div>
        <div class="variant-divider"></div>
        <p class="product-name">Men's<br>Natural Therapeutic<br>INTIMATE Wash</p>
      </div>
    </div>
    <div class="tube-cap"><div class="cap-lid"></div></div>
  </article>

</main>
</body>
</html>
```